Looking to design a new sign for our church.

Looking for a new sign
4 x 8 feet dimension
We are renaming the church "Medlow Ridge Community Church"
looking for legible graphics
Would like some type of backdrop being a family tree (oak) / open to other ideas as you are led
I have included a pic of the old sign for your review
would like to incorporate our ministry logo on the lower right hand corner of the sign / see file attached

```html
<!DOCTYPE html>
<html lang="en">
<head>
<meta charset="utf-8">
<title>Medlow Ridge Community Church – Sign</title>
<link href="https://fonts.googleapis.com/css2?family=Overlock:wght@900&family=Saira+Condensed:wght@300;700&display=swap" rel="stylesheet">
<style>
  :root {
    --navy: #282c5a;
    --navy-band: #2f2d78;
    --navy-band-dark: #24245e;
    --white: #ffffff;
    --panel-grey: #ececef;
    --gold-dark: #6b5530;
    --gold-light: #d8c08e;
    --backdrop: #eef0f2;
  }
  html, body {
    margin: 0;
    width: 1200px;
    height: 1117px;
    overflow: hidden;
    background: var(--backdrop);
  }
  .sign {
    position: absolute;
    left: 40px;
    top: 272px;
    width: 1120px;
    height: 572px;
    box-sizing: border-box;
    border: 12px solid var(--navy);
    background: linear-gradient(180deg, var(--panel-grey) 0%, var(--white) 30%, var(--white) 100%);
    overflow: hidden;
  }
  .sign__title {
    position: absolute;
    left: 0;
    right: 0;
    top: 38px;
    margin: 0;
    text-align: center;
    font-family: "Overlock", sans-serif;
    font-weight: 900;
    font-size: 98px;
    line-height: 96px;
    color: var(--navy);
    letter-spacing: -0.5px;
  }
  .sign__rule {
    position: absolute;
    left: 0;
    top: 270px;
    width: 724px;
    height: 10px;
    border-radius: 0 5px 5px 0;
    background: linear-gradient(90deg, var(--gold-dark) 0%, var(--gold-light) 22%, var(--gold-dark) 55%, #5a4526 100%);
  }
  .sign__band {
    position: absolute;
    left: 0;
    top: 295px;
    width: 790px;
    bottom: 0;
    background: radial-gradient(ellipse at 45% 40%, var(--navy-band) 0%, var(--navy-band-dark) 100%);
  }
  .schedule {
    position: absolute;
    left: 75px;
    top: 332px;
    margin: 0;
    padding: 0;
    list-style: none;
    font-family: "Saira Condensed", sans-serif;
    font-size: 56px;
    line-height: 59px;
    color: var(--white);
    letter-spacing: -0.5px;
  }
  .schedule__time { font-weight: 700; }
  .schedule__event { font-weight: 300; }
  .sign__tree {
    position: absolute;
    left: 651px;
    top: 276px;
    width: 304px;
    height: 272px;
    background: var(--navy);
    border-radius: 48% 48% 8% 8% / 62% 62% 6% 6%;
  }
  .ministry-mark {
    position: absolute;
    left: 952px;
    top: 300px;
    width: 130px;
    height: 240px;
    display: flex;
    flex-direction: column;
    align-items: center;
    justify-content: flex-end;
    gap: 10px;
  }
  .ministry-mark__dot {
    width: 70px;
    height: 70px;
    border-radius: 50%;
    background: var(--navy);
  }
  .ministry-mark__name {
    font-family: "Overlock", sans-serif;
    font-weight: 900;
    font-size: 20px;
    line-height: 22px;
    text-align: center;
    color: var(--navy);
  }
</style>
</head>
<body>
  <main class="sign">
    <h1 class="sign__title">Medlow Ridge<br>Community Church</h1>
    <div class="sign__rule"></div>
    <div class="sign__band"></div>
    <ul class="schedule">
      <li><span class="schedule__time">9:30AM</span> <span class="schedule__event">Sunday School</span></li>
      <li><span class="schedule__time">6:00PM</span> <span class="schedule__event">Wednesday Service</span></li>
      <li><span class="schedule__time">10:30AM</span> <span class="schedule__event">Worship Service</span></li>
    </ul>
    <div class="sign__tree" role="img" aria-label="Silhouette of a broad oak tree in navy"></div>
    <div class="ministry-mark">
      <div class="ministry-mark__dot"></div>
      <div class="ministry-mark__name">Crestway<br>Mission</div>
    </div>
  </main>
</body>
</html>
```